R&t Subterra

We specialize in CIPP pipe lining but do other underground utilities trenchless as well.

Target Market(s)

Trenchless sewer replacement

Contact Information for Business Card

Gavin Holtby 715-482-6130 Birchwood Flats, wi

```html
<!DOCTYPE html>
<html lang="en">
<head>
<meta charset="utf-8">
<title>R&amp;t Subterra — Business Card</title>
<link href="https://fonts.googleapis.com/css2?family=Montserrat:wght@700&family=Arimo:wght@400&display=swap" rel="stylesheet">
<style>
  :root {
    --page-bg: #e9e6e1;
    --card-white: #ffffff;
    --card-white-shade: #ececec;
    --brand-blue: #2a86c8;
    --blue-light: #4aa3d6;
    --blue-deep: #0d4d74;
    --rule-blue: #7fb8e2;
    --ink: #3a3a3a;
  }
  * { box-sizing: border-box; margin: 0; padding: 0; }
  html, body { width: 1200px; height: 900px; overflow: hidden; }
  body {
    background: var(--page-bg);
    display: flex;
    flex-direction: column;
    align-items: center;
    justify-content: center;
    gap: 44px;
  }
  .card {
    width: 680px;
    height: 388px;
    border-radius: 30px;
    position: relative;
    box-shadow: 0 10px 28px rgba(0,0,0,0.22);
    overflow: hidden;
  }
  .card--back {
    background: radial-gradient(ellipse at 50% 45%, var(--blue-light) 0%, #2f86ba 45%, var(--blue-deep) 100%);
    display: flex;
    align-items: center;
    justify-content: center;
  }
  .brand {
    display: flex;
    align-items: center;
    gap: 16px;
    font-family: "Montserrat", sans-serif;
    font-weight: 700;
  }
  .brand__dot { border-radius: 50%; flex: none; }
  .card--back .brand { color: #1b6fb0; font-size: 46px; }
  .card--back .brand__dot { width: 40px; height: 40px; background: #1b6fb0; }

  .card--front {
    background: linear-gradient(120deg, var(--card-white-shade) 0%, var(--card-white) 55%, #f4f4f4 100%);
  }
  .card--front .brand {
    position: absolute;
    top: 96px;
    left: 0; right: 0;
    justify-content: center;
    color: var(--brand-blue);
    font-size: 50px;
  }
  .card--front .brand__dot { width: 46px; height: 46px; background: var(--brand-blue); }

  .name-row {
    position: absolute;
    top: 212px;
    left: 70px; right: 70px;
    display: flex;
    align-items: center;
    gap: 14px;
  }
  .rule { flex: 1; height: 1px; background: var(--rule-blue); }
  .person-name {
    font-family: "Montserrat", sans-serif;
    font-weight: 700;
    font-size: 22px;
    letter-spacing: 0.5px;
    color: var(--brand-blue);
    text-transform: uppercase;
  }
  .contact {
    position: absolute;
    top: 260px;
    left: 0; right: 0;
    display: flex;
    justify-content: center;
    align-items: center;
    gap: 8px;
    font-family: "Arimo", sans-serif;
    font-size: 20px;
    color: var(--ink);
  }
  .contact svg { width: 18px; height: 18px; fill: var(--brand-blue); }
</style>
</head>
<body>
  <section class="card card--back" aria-label="Card back">
    <div class="brand"><span class="brand__dot"></span>R&amp;t Subterra</div>
  </section>

  <section class="card card--front" aria-label="Card front">
    <div class="brand"><span class="brand__dot"></span>R&amp;t Subterra</div>

    <div class="name-row">
      <span class="rule"></span>
      <span class="person-name">Gavin Holtby</span>
      <span class="rule"></span>
    </div>

    <div class="contact">
      <svg viewBox="0 0 24 24" aria-hidden="true"><path d="M6.6 10.8a15.1 15.1 0 0 0 6.6 6.6l2.2-2.2c.3-.3.7-.4 1-.2 1.1.4 2.3.6 3.6.6.6 0 1 .4 1 1V20c0 .6-.4 1-1 1A17 17 0 0 1 3 4c0-.6.4-1 1-1h3.5c.6 0 1 .4 1 1 0 1.3.2 2.5.6 3.6.1.3 0 .7-.2 1z"/></svg>
      <span class="phone">715-482-6130</span>
      <span class="sep">|</span>
      <svg viewBox="0 0 24 24" aria-hidden="true"><path d="M12 2a7 7 0 0 0-7 7c0 5.2 7 13 7 13s7-7.8 7-13a7 7 0 0 0-7-7zm0 9.5A2.5 2.5 0 1 1 12 6.5a2.5 2.5 0 0 1 0 5z"/></svg>
      <span class="location">Birchwood Flats, wi</span>
    </div>
  </section>
</body>
</html>
```